Business card for Eyelash extension salon in Westmere,California USA

We need new business card for our salon in Westmere. The salon name is 'Lumarra' . We would like to have...Business name: Lumarra Name of person: will provide later Address 6128 N.Corbel Ridge Blvd Westmere , CA 90471 Phone: will provide later (Text only) Web: www.lumarrastudio-example.com Pictogrid icon, Friendvale icon follow us for seasonal campaign and news @lumarrastudioexample Design should look elegant, high-end, clean, simple, cohesive with my brand. Please refer my brand board. Business name color will be metallic bronzy color. Im thinking grey background or white background. Thanks

Target Market(s)

25-35. Gender neutral. People who are in Entertainment business industry.
This is High-end Eyelash extension salon in Westmere

Industry/Entity Type

Beauty Salon

Contact Information for Business Card

Business name: Lumarra
Name of person: will provide later
Address 6128 N.Corbel Ridge Blvd Westmere , CA 90471
Phone: will provide later (Text only)
Web: www.lumarrastudio-example.com
Pictogrid icon, Friendvale icon
follow us for seasonal campaign and news @lumarrastudioexample

Requirements
Must have
• Beautiful, elegant, clean and simple look but very attractive and modern
Should not have
• We don't like too clutter, too busy designs.

```html
<!DOCTYPE html>
<html lang="en">
<head>
<meta charset="utf-8">
<title>Lumarra Business Card</title>
<link rel="stylesheet" href="https://fonts.googleapis.com/css2?family=Bodoni+Moda:wght@400;600&family=Cormorant+Garamond:wght@400;500&family=Josefin+Sans:wght@400&display=swap">
<style>
  :root {
    --bg: #efece6;
    --card-white: #ffffff;
    --bronze: #8a6850;
    --ink: #3b3330;
    --white: #ffffff;
    --shadow: 0 3px 8px rgba(0,0,0,0.22);
  }
  * { margin: 0; padding: 0; box-sizing: border-box; }
  html, body {
    width: 1200px; height: 930px; overflow: hidden;
    background: var(--bg);
  }
  .stage { position: relative; width: 1200px; height: 930px; }

  .card {
    position: absolute;
    left: 318px; width: 564px; height: 323px;
    box-shadow: var(--shadow);
    overflow: hidden;
  }
  .card--front { top: 125px; background: var(--card-white); }
  .card--back { top: 514px; background: var(--bronze); }

  .brand-name {
    font-family: "Bodoni Moda", serif;
    font-weight: 400;
    line-height: 1;
  }
  .brand-place {
    font-family: "Josefin Sans", sans-serif;
    letter-spacing: 0.18em;
    text-transform: uppercase;
  }

  .front-brand { position: absolute; left: 26px; top: 36px; color: var(--bronze); }
  .front-brand .brand-name { font-size: 50px; }
  .front-brand .brand-place { font-size: 7px; color: var(--bronze); margin: 8px 0 0 86px; }

  .holder { position: absolute; left: 27px; top: 148px; }
  .holder-name {
    font-family: "Bodoni Moda", serif;
    font-weight: 600;
    font-size: 26px;
    color: var(--bronze);
    line-height: 1;
  }
  .holder-role {
    font-family: "Cormorant Garamond", serif;
    font-size: 15px;
    color: var(--ink);
    margin-top: 3px;
  }

  .address {
    position: absolute; left: 27px; top: 200px;
    font-family: "Cormorant Garamond", serif;
    font-style: normal;
    font-weight: 500;
    font-size: 15px; line-height: 19px;
    color: var(--ink);
  }

  .contacts {
    position: absolute; left: 27px; top: 251px;
    list-style: none;
    font-family: "Cormorant Garamond", serif;
    font-weight: 500;
    font-size: 15px; line-height: 19px;
    color: var(--ink);
  }
  .contacts li { display: flex; align-items: center; gap: 8px; }
  .contacts svg { width: 9px; height: 9px; flex: none; }

  .portrait {
    position: absolute; right: 0; top: 0;
    width: 284px; height: 323px;
    background:
      radial-gradient(ellipse 62% 70% at 50% 62%, #f4f4f4 0%, #e6e6e6 60%, rgba(230,230,230,0) 72%),
      linear-gradient(180deg, #1c1c1c 0%, #2a2a2a 14%, #f1f1f1 30%, #fafafa 100%);
  }

  .back-brand {
    position: absolute; left: 0; right: 0; top: 112px;
    text-align: center; color: var(--white);
  }
  .back-brand .brand-name { font-size: 72px; }
  .back-brand .brand-place { font-size: 10px; margin: 12px 0 0 90px; }
</style>
</head>
<body>
<main class="stage">
  <section class="card card--front">
    <div class="front-brand">
      <div class="brand-name">Lumarra</div>
      <div class="brand-place">Westmere</div>
    </div>

    <div class="holder">
      <div class="holder-name">Elena R. Moreno</div>
      <div class="holder-role">Director</div>
    </div>

    <address class="address">
      6128 N.Corbel Ridge<br>
      Blvd Westmere , CA 90471
    </address>

    <ul class="contacts">
      <li>
        <svg viewBox="0 0 10 10" aria-hidden="true"><path d="M2.2 0.8 L3.6 2.6 L2.8 3.6 Q3.8 5.9 6.2 7.1 L7.2 6.3 L9.1 7.7 L8.2 9.3 Q3.8 9 0.8 1.8 Z" fill="var(--bronze)"/></svg>
        555.201.0147
      </li>
      <li>
        <svg viewBox="0 0 10 10" aria-hidden="true"><rect x="0.7" y="2" width="8.6" height="6" fill="none" stroke="var(--bronze)" stroke-width="1.1"/><path d="M0.9 2.4 L5 5.4 L9.1 2.4" fill="none" stroke="var(--bronze)" stroke-width="1.1"/></svg>
        studio.lumarra@example.com
      </li>
      <li>
        <svg viewBox="0 0 10 10" aria-hidden="true"><g fill="none" stroke="var(--bronze)" stroke-width="0.9"><circle cx="5" cy="5" r="4.2"/><ellipse cx="5" cy="5" rx="1.9" ry="4.2"/><path d="M0.8 5 H9.2 M1.5 3 H8.5 M1.5 7 H8.5"/></g></svg>
        www.lumarrastudio-example.com
      </li>
    </ul>

    <div class="portrait" role="img" aria-label="Black and white beauty portrait showing long lash extensions on closed eyes"></div>
  </section>

  <section class="card card--back">
    <div class="back-brand">
      <div class="brand-name">Lumarra</div>
      <div class="brand-place">Westmere</div>
    </div>
  </section>
</main>
</body>
</html>
```